Flyer Design Needed for 6th Annual Rise Together Summit

5th Annual Rise Together Summit
by the Council for Stewardship in Civic Works (C-SwCW)
Theme: Bold Horizons Ahead
Date: May 14, 2020
Location: VIRTUAL
#BoldHorizonsAhead

This is event is put together by C-SwCW's Rise Together Guild of Distinction. I have a logo for the Guild of Distinction, but not something that indicates it's the Rise Together Guild.

More about the Forum (please don't include on the flyer): This Forum provides a venue to openly discuss issues affecting women in our industry and ideas and strategies to address those issues.

Architecture, Construction and Engineering are all struggling with a tremendous shortage of skilled talent. It is more important than ever for organizations to be able to attract, support and retain a talented workforce and to encourage more women to pursue and build vibrant careers in architecture, engineering and construction. Unfortunately, their attrition rate also remains high in these industries. Developing and retaining a skilled workforce includes identifying and addressing the specific needs of women in our industry. Man or Woman; Male or Female Brain, C-SwCW’s Rise Together Summit will give you and your team the tools you need to excel as an Employer of Choice and a roadmap for individual continued career planning and success .

This unique Forum provides a venue to engage everyone from executives to those just beginning their careers with active, hands-on sessions and vibrant networking with the best and brightest in the A/E/C industry. Join local, state and national leaders and subject matter experts as we candidly explore and address the issues affecting women in our industry .
Updates

We really like the design attached, but the profile of the woman is not what we're looking for and we don't want the pink. We do like that she is overseeing the buildings, and architecture. Would love the image of a woman in a power pose who is half dressed in her field gear and half dressed in her office clothes. Half and half – business attire and site gear. Power pose with hands on hips,

Target Market(s)

Women in the Design and Construction Industry

Font styles to use
Sans Serif

Requirements
Must have
• Date, location
Nice to have
• We really like the design attached, but the profile of the woman is not what we're looking for and we don't want the pink. We do like that she is overseeing the buildings, and architecture.

Would love the image of a woman in a power pose who is half dressed in her field gear and half dressed in her office clothes.
Half and half – business attire and site gear.
Power pose with hands on hips,

```html
<!DOCTYPE html>
<html lang="en">
<head>
<meta charset="utf-8">
<title>Rise Together Summit Flyer</title>
<link rel="stylesheet" href="https://fonts.googleapis.com/css2?family=Montserrat:wght@300;500;600;800&display=swap">
<style>
  :root {
    --navy: #20318a;
    --charcoal: #4a4a4c;
    --green: #8fbb3c;
    --sky: #cfe6f5;
    --sky-deep: #5e9fd6;
    --paper: #ffffff;
    --stage: #e4e4e4;
    --text: #1c1c1c;
  }
  * { margin: 0; padding: 0; box-sizing: border-box; }
  html, body { width: 1200px; height: 776px; overflow: hidden; }
  body {
    background: var(--stage);
    font-family: "Montserrat", Arial, sans-serif;
    position: relative;
  }
  .flyer {
    position: absolute;
    left: 344px; top: 28px;
    width: 511px; height: 720px;
    background: var(--paper);
    overflow: hidden;
  }
  .flyer__backdrop {
    position: absolute; inset: 0 0 20px 0;
    background:
      linear-gradient(180deg, rgba(255,255,255,0) 0%, rgba(255,255,255,0.85) 40%, rgba(255,255,255,0.6) 52%, rgba(255,255,255,0) 70%),
      linear-gradient(180deg, var(--sky) 0%, #eef6fc 35%, #d9ebf8 60%, var(--sky-deep) 100%);
  }
  .brand-box {
    position: absolute;
    left: 143px; top: 0;
    width: 226px; height: 118px;
    background: var(--paper);
    display: flex; align-items: center; justify-content: center;
    gap: 12px;
    padding: 0 8px;
  }
  .brand {
    display: flex; flex-direction: column; align-items: center; gap: 5px;
  }
  .brand__dot {
    width: 26px; height: 26px; border-radius: 50%;
    background: var(--navy);
  }
  .brand__name {
    font-size: 10.5px; font-weight: 600; color: var(--navy);
    white-space: nowrap;
  }
  .brand__sub {
    font-size: 4.5px; font-weight: 500; color: var(--navy);
    white-space: nowrap;
  }
  .title {
    position: absolute; left: 0; right: 0; top: 244px;
    text-align: center; line-height: 1;
  }
  .title__lead {
    display: block;
    font-size: 28px; font-weight: 300; color: var(--charcoal);
    letter-spacing: 1px;
  }
  .title__main {
    display: block;
    font-size: 60px; font-weight: 800; color: var(--navy);
    letter-spacing: -1px; margin-top: 6px;
  }
  .title__tail {
    display: block;
    font-size: 50px; font-weight: 800; color: var(--charcoal);
    margin-top: 4px;
  }
  .host-band {
    position: absolute; left: 66px; top: 409px;
    width: 379px; height: 25px;
    background: var(--green);
    clip-path: polygon(3% 0, 100% 0, 97% 100%, 0 100%);
    display: flex; align-items: center; justify-content: center;
    font-size: 10.5px; font-weight: 500; color: var(--text);
  }
  .details {
    position: absolute; left: 0; right: 0; top: 553px;
  }
  .detail {
    position: absolute; width: 130px; margin-left: -65px;
    display: flex; flex-direction: column; align-items: center;
    text-align: center; font-size: 11.5px; line-height: 1.25; color: var(--text);
  }
  .detail svg { width: 44px; height: 44px; margin-bottom: 12px; }
  .detail__label { font-weight: 600; font-size: 12.5px; }
  .detail--theme { left: 106px; }
  .detail--date { left: 235px; }
  .detail--place { left: 336px; }
  .detail--tag { left: 433px; }
  .footer-bar {
    position: absolute; left: 0; right: 0; bottom: 0; height: 20px;
    background: var(--green);
  }
</style>
</head>
<body>
  <main class="flyer">
    <div class="flyer__backdrop" role="img" aria-label="Soft blue city skyline of glass towers reflected in water"></div>

    <header class="brand-box">
      <div class="brand">
        <span class="brand__dot"></span>
        <span class="brand__name">C-SwCW</span>
        <span class="brand__sub">Council for Stewardship in Civic Works</span>
      </div>
      <div class="brand">
        <span class="brand__dot"></span>
        <span class="brand__name">Guild of Distinction</span>
        <span class="brand__sub">Council for Stewardship in Civic Works</span>
      </div>
    </header>

    <h1 class="title">
      <span class="title__lead">RISE</span>
      <span class="title__main">TOGETHER</span>
      <span class="title__tail">SUMMIT</span>
    </h1>

    <p class="host-band">by the Council for Stewardship in Civic Works (C-SwCW)</p>

    <section class="details">
      <div class="detail detail--theme">
        <svg viewBox="0 0 44 44" aria-hidden="true">
          <circle cx="22" cy="22" r="22" fill="var(--navy)"/>
          <g fill="none" stroke="#fff" stroke-width="1.8" stroke-linecap="round" stroke-linejoin="round">
            <path d="M22 13 c-2-2-6-2-7 1 c-3 0-4 3-3 5 c-2 1-2 4 0 5 c-1 2 1 5 3 4 c1 2 4 3 7 1z"/>
            <path d="M22 13 c2-2 6-2 7 1 c3 0 4 3 3 5 c2 1 2 4 0 5 c1 2-1 5-3 4 c-1 2-4 3-7 1z"/>
            <line x1="22" y1="13" x2="22" y2="31"/>
            <path d="M16 19 c2 0 3 1 3 3 M28 19 c-2 0-3 1-3 3 M16 25 c2 0 3-1 4 0 M28 25 c-2 0-3-1-4 0"/>
          </g>
        </svg>
        <span class="detail__label">Theme:</span>
        <span>Bold Horizons Ahead</span>
      </div>
      <div class="detail detail--date">
        <svg viewBox="0 0 44 44" aria-hidden="true">
          <circle cx="22" cy="22" r="22" fill="var(--navy)"/>
          <rect x="12" y="14" width="20" height="17" rx="2" fill="none" stroke="#fff" stroke-width="2"/>
          <line x1="12" y1="19" x2="32" y2="19" stroke="#fff" stroke-width="2"/>
          <line x1="16" y1="11" x2="16" y2="16" stroke="#fff" stroke-width="2"/>
          <line x1="28" y1="11" x2="28" y2="16" stroke="#fff" stroke-width="2"/>
          <g fill="#fff"><rect x="15" y="22" width="3" height="2"/><rect x="20.5" y="22" width="3" height="2"/><rect x="26" y="22" width="3" height="2"/><rect x="15" y="26" width="3" height="2"/><rect x="20.5" y="26" width="3" height="2"/><rect x="26" y="26" width="3" height="2"/></g>
        </svg>
        <span class="detail__label">Date:</span>
        <span>May 14, 2020</span>
      </div>
      <div class="detail detail--place">
        <svg viewBox="0 0 44 44" aria-hidden="true">
          <circle cx="22" cy="22" r="22" fill="var(--navy)"/>
          <path d="M22 33 C17 26 15 23 15 19 a7 7 0 0 1 14 0 c0 4 -2 7 -7 14z" fill="none" stroke="#fff" stroke-width="2"/>
          <circle cx="22" cy="19" r="2.5" fill="#fff"/>
        </svg>
        <span class="detail__label">Location:</span>
        <span>VIRTUAL</span>
      </div>
      <div class="detail detail--tag">
        <svg viewBox="0 0 44 44" aria-hidden="true">
          <circle cx="22" cy="22" r="22" fill="var(--navy)"/>
          <text x="22" y="30" text-anchor="middle" font-family="Montserrat, Arial, sans-serif" font-weight="800" font-size="22" fill="#fff">#</text>
        </svg>
        <span>Bold Horizons</span>
        <span>Ahead</span>
      </div>
    </section>

    <div class="footer-bar"></div>
  </main>
</body>
</html>
```